Landing page graphical layout.

New landing page to capture leads from homeowners who are interested in learning the value of their home and/or selling their home.
The page should have a picture of a home in a residential area, possibly with a family standing outside.
This is the client's current site: http://homeworthpulse.com/
As you can see, it is very limited in terms of text and design, however once the user fills in the field it takes them to another page. The page's graphics should be enhanced with more calls to action as well as an additional field for the email address.
The client is a lead generator for real estate agents, so do not put the company name on the site as it will be used as a template for the client's various sites.
The forms need to be duplicated and inserted into the new design.
Some example sites:
http://www.brindlo.com/how-much-is-my-home-worth/
http://www.kptroost.com/home-valuation/?source=PROMO_SELLER&gclid=XQwerT_b-zzKLMnopqrS4B1
https://www.plovara.com/what-is-my-home-worth?estPropertyId=4190827&src=landing-page
Thanks!
Industry/Entity Type
Real Estate
Number of Pages Required
1 page
Look and feel

```html
<!DOCTYPE html>
<html lang="en">
<head>
<meta charset="utf-8">
<title>Get Your Home Value Estimate</title>
<link rel="stylesheet" href="https://fonts.googleapis.com/css2?family=Ubuntu:wght@400;500;700&display=swap">
<style>
  :root {
    --blue: #29a9e1;
    --blue-dark: #1b8fc4;
    --green: #8cc63f;
    --green-light: #a5d65a;
    --charcoal: #555759;
    --band: #ececec;
    --field-border: #d5d5d5;
    --text: #666;
    --white: #fff;
  }
  * { box-sizing: border-box; margin: 0; padding: 0; }
  html, body { width: 800px; height: 1200px; overflow: hidden; }
  body { font-family: "Ubuntu", Arial, sans-serif; background: var(--white); color: var(--text); position: relative; }

  .site-header { height: 75px; background: var(--blue); display: flex; align-items: center; justify-content: center; }
  .site-header h1 { color: var(--white); font-size: 27px; font-weight: 500; letter-spacing: .5px; }

  .hero-photo { height: 325px; background: linear-gradient(180deg, #c9c2b8 0%, #a8867a 40%, #8a5a4c 70%, #b9b4aa 100%); }

  .steps-intro { height: 85px; display: flex; align-items: center; justify-content: center; }
  .steps-intro h2 { font-size: 22px; font-weight: 500; color: var(--green); }
  .steps-intro h2 span { color: var(--blue); }

  .estimate-band { height: 315px; background: var(--band); padding: 27px 0 0 88px; }
  .step-tabs { display: flex; gap: 6px; }
  .step-tab { height: 29px; width: 152px; display: flex; align-items: center; justify-content: center; color: var(--white); font-size: 11px; font-weight: 500; text-transform: uppercase; border-radius: 4px 4px 0 0; }
  .step-tab.done { background: var(--blue); }
  .step-tab.current { background: var(--green); width: 136px; }
  .step-tab.next { background: var(--charcoal); width: 139px; }

  .step-panel { width: 627px; height: 246px; background: var(--green); position: relative; padding: 8px 13px; }
  .step-title { color: var(--white); font-size: 34px; font-weight: 500; line-height: 40px; }
  .step-note { position: absolute; left: 187px; top: 14px; color: var(--white); font-size: 11px; }

  .detail-fields { width: 160px; margin-top: 4px; display: grid; grid-template-columns: 1fr 1fr; column-gap: 8px; row-gap: 3px; }
  .detail-fields .full { grid-column: 1 / 3; }
  .detail-fields label { display: block; color: var(--white); font-size: 8px; margin-bottom: 2px; }
  .detail-fields .box { height: 18px; background: var(--white); border-radius: 2px; font-size: 8px; color: #888; padding: 4px 5px; display: flex; justify-content: space-between; }
  .detail-fields .box.select::after { content: "▾"; color: #999; }
  .confirm-btn { margin-top: 8px; width: 160px; height: 20px; background: var(--blue); color: var(--white); border: 0; font: 500 9px "Ubuntu", Arial, sans-serif; text-transform: uppercase; }

  .street-photo { position: absolute; left: 187px; top: 51px; width: 426px; height: 181px; background: linear-gradient(180deg, #b8c8d6 0%, #a59485 45%, #8c8a86 75%, #6e6e6c 100%); }

  .consultation { height: 363px; text-align: center; padding-top: 22px; }
  .consultation h2 { color: var(--green); font-size: 22px; font-weight: 500; }
  .consultation p { width: 370px; margin: 10px auto 0; font-size: 12px; line-height: 17px; color: var(--green); }
  .lead-form { width: 440px; margin: 20px auto 0; text-align: left; }
  .lead-form .row { display: flex; gap: 12px; margin-bottom: 10px; }
  .lead-form .field { flex: 1; height: 24px; border: 1px solid var(--field-border); font-size: 9px; color: #999; padding: 6px 7px; }
  .lead-form .label { font-size: 9px; color: var(--text); margin: -2px 0 3px; }
  .lead-form .notes { height: 50px; }
  .send-btn { display: block; margin: 14px auto 0; width: 140px; height: 28px; background: var(--blue); color: var(--white); border: 0; font: 500 13px "Ubuntu", Arial, sans-serif; text-transform: uppercase; }

  .site-footer { position: absolute; left: 0; bottom: 0; width: 800px; height: 37px; background: var(--charcoal); color: #ddd; font-size: 10px; display: flex; align-items: center; justify-content: center; }
</style>
</head>
<body>
  <header class="site-header"><h1>GET YOUR HOME VALUE ESTIMATE</h1></header>

  <div class="hero-photo" role="img" aria-label="Photo of a young family sitting on the front steps of their brick home"></div>

  <section class="steps-intro"><h2>FIND YOUR HOME VALUE IN <span>THREE EASY STEPS</span></h2></section>

  <section class="estimate-band">
    <nav class="step-tabs">
      <div class="step-tab done">Your Address</div>
      <div class="step-tab current">Your Information</div>
      <div class="step-tab next">Your Home Value</div>
    </nav>
    <div class="step-panel">
      <div class="step-title">STEP TWO</div>
      <div class="step-note">Find your home value right now by simply confirming information about your home</div>
      <div class="detail-fields">
        <div class="full"><label>Property Type</label><div class="box select">Single Family Home</div></div>
        <div><label>Bedrooms</label><div class="box select">3</div></div>
        <div><label>Bathrooms</label><div class="box select">2</div></div>
        <div><label>Square Feet</label><div class="box">1,850</div></div>
        <div><label>Year Built</label><div class="box">1998</div></div>
        <div><label>Lot Size</label><div class="box">0.25</div></div>
        <div><label>Garage</label><div class="box select">2 Car</div></div>
      </div>
      <button class="confirm-btn">Confirm Your Details</button>
      <div class="street-photo" role="img" aria-label="Street view photo of the property and neighbouring buildings"></div>
    </div>
  </section>

  <section class="consultation">
    <h2>GET A NO-OBLIGATION CONSULTATION</h2>
    <p>A local Agent can send you a professional comparative market analysis (CMA) for this home. It's free, with no obligation</p>
    <div class="lead-form">
      <div class="row"><div class="field">First Name</div><div class="field">Last Name</div></div>
      <div class="row"><div class="field">Email</div><div class="field">Phone</div></div>
      <div class="label">Prepare a Professional CMA for:</div>
      <div class="row"><div class="field"></div></div>
      <div class="row"><div class="field notes">Comments/Notes</div></div>
    </div>
    <button class="send-btn">Send Request</button>
  </section>

  <footer class="site-footer">© 2015, All rights reserved.</footer>
</body>
</html>
```